BrimTaps.com

Hey guys!

We are looking for an innovative 1 page web design for our PPC network website - http://quickpanelgrab.example/4k7rw2mz8q
We are a PPC social media start up, which works with many social media publishers worldwide.
The design must be clean, flat, trendy, we would like to keep our 1 page design structure, but add your own personal touch-up.

We would like you to make it look like a Million $ company.

Good luck!

Target Market(s)

Big Internet Advertising Companies

Number of Pages Required

1 page

```html
<!DOCTYPE html>
<html lang="en">
<head>
<meta charset="utf-8">
<title>Social Media Enterprise</title>
<link rel="stylesheet" href="https://fonts.googleapis.com/css2?family=Arimo:ital,wght@0,400;0,700;1,400;1,700&family=Oswald:wght@500&display=swap">
<style>
:root{
  --page-bg:#ffffff;
  --header-blue:#2b22fb;
  --crescent:#6a5cff;
  --globe-light:#5fd0ee;
  --globe-dark:#0b5d9a;
  --bar-black:#161616;
  --mid-grey:#6e6d6e;
  --dark-grey:#3f3f3f;
  --footer-grey:#2f2f2f;
  --lavender:#a9a8f0;
  --lavender-soft:#d4d0f8;
  --green:#9ef97f;
  --green-edge:#6fd85a;
  --salmon:#fc6f69;
  --white:#ffffff;
  --ink:#222222;
}
*{box-sizing:border-box;margin:0;padding:0}
html,body{width:1200px;height:1000px;overflow:hidden;background:var(--page-bg)}
body{font-family:"Arimo",Arial,sans-serif;color:var(--white)}
.page{position:absolute;left:333px;top:0;width:533px;height:1000px}
.band{position:absolute;left:0;width:533px}
.abs{position:absolute}

/* header */
.site-header{top:0;height:237px;background:var(--header-blue)}
.logo-slot{left:14px;top:10px;width:40px;font-size:13px;line-height:13px;text-align:center}
.site-title{left:114px;top:21px;font-size:21px;white-space:nowrap}
.hero-art{left:37px;top:20px;width:200px;height:195px}
.service-list{list-style:none}
.service-list li{position:absolute;font-size:7px;font-weight:700;white-space:nowrap}
.divider-curve{left:0;top:0}
.tagline{left:303px;top:56px;font-size:9px;white-space:nowrap}
.intro{left:326px;top:105px;width:172px;font-size:7px;line-height:8px}
.main-nav a{position:absolute;top:176px;font-family:"Oswald",sans-serif;font-size:9px;color:var(--white);text-decoration:none;white-space:nowrap}

/* social bar */
.social-bar{top:237px;height:28px;background:var(--bar-black)}
.social-link{position:absolute;top:9px;width:60px;display:flex;align-items:center;justify-content:center;gap:3px;font-size:7px;font-weight:700;color:var(--white)}
.social-link i{display:block;width:8px;height:8px;background:var(--lavender)}

/* features */
.features{top:265px;height:211px;background:var(--mid-grey)}
.feature-frame{position:absolute;top:37px;width:101px;height:56px;border:1px solid var(--white);border-radius:3px;background:#3a3a3a;padding:8px 8px}
.feature-image{width:100%;height:100%}
.feature-title{position:absolute;top:104px;font-size:9px;font-style:italic;font-weight:700;color:var(--lavender)}
.feature-text{position:absolute;top:124px;width:101px;font-size:5.6px;line-height:6.9px;text-align:justify;color:#eeeeee}

.mission{top:476px;height:29px;background:var(--bar-black);font-size:7px;font-style:italic;text-align:center;padding-top:5px}

/* widgets */
.widgets{top:505px;height:246px;background:var(--dark-grey)}
.widget-heading{position:absolute;top:28px;font-size:8px;font-weight:700}
.widget-panel{position:absolute;top:47px;height:167px;border-radius:3px}
.panel-green{background:var(--green);border:1px solid var(--green-edge);box-shadow:0 2px 0 var(--green-edge)}
.panel-salmon{background:var(--salmon);border:1px solid var(--white)}
.scroll-button{position:absolute;left:45px;width:41px;height:11px;border-radius:6px;background:var(--lavender);border:1px solid #7f7edb}
.scroll-button svg{display:block;margin:1px auto 0}
.article{position:absolute;left:6px;width:119px;height:27px;border-radius:3px;background:var(--mid-grey);padding:2px 7px}
.article h4{font-size:7px;font-weight:400;font-style:italic;color:var(--lavender);white-space:nowrap}
.article p{font-size:4.4px;line-height:5px;color:var(--white)}
.comment{position:absolute;left:9px;width:128px;height:45px;border-radius:4px;background:var(--lavender-soft);color:var(--ink);padding:3px 5px 0 25px}
.avatar{position:absolute;left:6px;top:4px;width:16px;height:17px;background:#9a95ea;border-radius:2px}
.comment p{font-size:4.4px;line-height:5px}
.comment-meta{position:absolute;left:25px;right:5px;bottom:3px;display:flex;gap:6px;font-size:4.4px;font-style:italic}
.comment-meta .actions{margin-left:auto;display:flex;gap:7px}
.scroll-track{position:absolute;top:6px;width:4px;border-radius:2px;background:#555555}
.event{position:absolute;left:8px;width:115px;color:var(--ink)}
.event h4{font-size:6px;font-weight:700}
.event h5{font-size:5px;font-weight:700;margin-top:1px}
.event p{font-size:4.2px;line-height:5px;margin-top:3px}
.event time{display:block;font-size:4.2px;margin-top:3px}
.event-rule{position:absolute;left:8px;width:109px;height:2px;background:var(--ink)}

/* footer */
.footer-nav{top:751px;height:59px;background:var(--mid-grey)}
.footer-nav span{position:absolute;top:21px;font-size:13px;white-space:nowrap}
.site-footer{top:810px;height:190px;background:var(--footer-grey)}
.footer-col{position:absolute;top:15px;list-style:none;font-size:6.5px;font-weight:700;line-height:12.7px}
.legal-box{position:absolute;left:259px;top:10px;width:130px;height:159px;border:1px solid var(--white);border-radius:6px;text-align:center;font-size:8px;font-weight:700}
.legal-box p{position:absolute;left:0;width:100%}
</style>
</head>
<body>
<div class="page">

  <header class="band site-header">
    <div class="abs logo-slot">Your Logo</div>
    <h1 class="abs site-title" style="font-weight:400">Social Media Enterprise</h1>
    <svg class="abs hero-art" viewBox="0 0 200 195" role="img" aria-label="Illustration of a blue world globe circled by a white orbit ring in front of a violet crescent">
      <defs>
        <radialGradient id="globeFill" cx="40%" cy="40%" r="65%">
          <stop offset="0" stop-color="var(--globe-light)"/>
          <stop offset="1" stop-color="var(--globe-dark)"/>
        </radialGradient>
      </defs>
      <ellipse cx="120" cy="103" rx="75" ry="80" fill="var(--crescent)"/>
      <circle cx="85" cy="105" r="72" fill="url(#globeFill)"/>
    </svg>
    <ul class="service-list">
      <li style="left:212px;top:56px">PPC Services</li>
      <li style="left:229px;top:71px">SEO</li>
      <li style="left:237px;top:89px">Keywords</li>
      <li style="left:242px;top:110px">Ad Services</li>
      <li style="left:240px;top:134px">Tracking</li>
      <li style="left:233px;top:156px">Advising</li>
      <li style="left:219px;top:177px">Reporting</li>
    </ul>
    <svg class="abs divider-curve" width="533" height="237" aria-hidden="true">
      <path d="M277 47 Q318 110 298 192" fill="none" stroke="var(--white)" stroke-width="1" opacity=".8"/>
    </svg>
    <p class="abs tagline">PPC Pay Per Clic Services</p>
    <p class="abs intro">Lorem ipsum dolor sit amet, consectetur adipisicing elit, sed do eiusmod tempor incididunt ut labore et dolore magna aliqua.</p>
    <nav class="main-nav">
      <a href="#" style="left:303px">Home</a>
      <a href="#" style="left:335px">Services</a>
      <a href="#" style="left:378px">Process</a>
      <a href="#" style="left:419px">Clients</a>
      <a href="#" style="left:454px">Contact</a>
      <a href="#" style="left:495px">About US</a>
    </nav>
  </header>

  <nav class="band social-bar">
    <span class="social-link" style="left:56px"><i></i>Friendlane</span>
    <span class="social-link" style="left:116px"><i></i>Vidora</span>
    <span class="social-link" style="left:178px"><i></i>Postly</span>
    <span class="social-link" style="left:238px"><i></i>Quipline</span>
    <span class="social-link" style="left:299px"><i></i>Hollr</span>
    <span class="social-link" style="left:361px"><i></i>Worknet</span>
    <span class="social-link" style="left:422px"><i></i>Roomly</span>
  </nav>

  <section class="band features">
    <div class="feature-frame" style="left:62px">
      <svg class="feature-image" role="img" aria-label="Photo of a glowing blue keyboard on black"><rect width="100%" height="100%" fill="#0a0a0a"/><rect x="8%" y="30%" width="84%" height="30%" fill="#2bb6e0" opacity=".7"/></svg>
    </div>
    <div class="feature-frame" style="left:218px">
      <svg class="feature-image" role="img" aria-label="Photo of a trading floor with a glowing orange display"><defs><linearGradient id="hall" x1="0" y1="0" x2="0" y2="1"><stop offset="0" stop-color="#d9582a"/><stop offset="1" stop-color="#2a2a5a"/></linearGradient></defs><rect width="100%" height="100%" fill="url(#hall)"/></svg>
    </div>
    <div class="feature-frame" style="left:375px">
      <svg class="feature-image" role="img" aria-label="Photo of a wall of many colourful screens"><defs><linearGradient id="wall" x1="0" y1="0" x2="1" y2="0"><stop offset="0" stop-color="#6a4a3a"/><stop offset=".5" stop-color="#c59a6a"/><stop offset="1" stop-color="#3a5a7a"/></linearGradient></defs><rect width="100%" height="100%" fill="url(#wall)"/></svg>
    </div>
    <h3 class="feature-title" style="left:62px">Marketing</h3>
    <h3 class="feature-title" style="left:218px">Analytics</h3>
    <h3 class="feature-title" style="left:377px">Media</h3>
    <p class="feature-text" style="left:62px">Lorem ipsum dolor sit amet, consectetur adipisicing elit, sed do eiusmod tempor incididunt ut labore et dolore magna aliqua. Ut enim ad minim veniam, quis nostrud exercitation ullamco laboris nisi ut aliquip ex ea commodo consequat.</p>
    <p class="feature-text" style="left:218px">Lorem ipsum dolor sit amet, consectetur adipisicing elit, sed do eiusmod tempor incididunt ut labore et dolore magna aliqua. Ut enim ad minim veniam, quis nostrud exercitation ullamco laboris nisi ut aliquip ex ea commodo consequat.</p>
    <p class="feature-text" style="left:377px">Lorem ipsum dolor sit amet, consectetur adipisicing elit, sed do eiusmod tempor incididunt ut labore et dolore magna aliqua. Ut enim ad minim veniam, quis nostrud exercitation ullamco laboris nisi ut aliquip ex ea commodo consequat.</p>
  </section>

  <p class="band mission">We are a PPC social media start up, which works with many social media publishers worldwide.</p>

  <section class="band widgets">
    <h2 class="widget-heading" style="left:28px">Most read</h2>
    <h2 class="widget-heading" style="left:203px">Comments</h2>
    <h2 class="widget-heading" style="left:383px">Upcomming Events</h2>

    <div class="widget-panel panel-green" style="left:22px;width:134px">
      <div class="scroll-button" style="top:3px"><svg width="14" height="8" aria-hidden="true"><path d="M2 7 L7 2 L12 7" fill="none" stroke="#111" stroke-width="2"/></svg></div>
      <article class="article" style="top:16px"><h4>PPC Market Evolution</h4><p>Lorem ipsum dolor sit amet, consectetur adipisicing elit, sed do eiusmod tempor incididunt ut labore et.</p></article>
      <article class="article" style="top:52px"><h4>500 Fortune most sucess enterprise</h4><p>Lorem ipsum dolor sit amet, consectetur adipisicing elit, sed do eiusmod tempor incididunt ut labore et.</p></article>
      <article class="article" style="top:88px"><h4>International online trading</h4><p>Lorem ipsum dolor sit amet, consectetur adipisicing elit, sed do eiusmod tempor incididunt ut labore et.</p></article>
      <article class="article" style="top:123px"><h4>SEO - New features</h4><p>Lorem ipsum dolor sit amet, consectetur adipisicing elit, sed do eiusmod tempor incididunt ut labore et.</p></article>
      <div class="scroll-button" style="top:152px"><svg width="14" height="8" aria-hidden="true"><path d="M2 2 L7 7 L12 2" fill="none" stroke="#111" stroke-width="2"/></svg></div>
    </div>

    <div class="widget-panel panel-salmon" style="left:198px;width:150px;top:46px;height:169px">
      <div class="comment" style="top:5px"><span class="avatar"></span><p>Lorem ipsum dolor sit amet, consectetur adipisicing elit, sed do eiusmod tempor incididunt ut labore et dolore magna aliqua. Ut enim ad minim veniam.</p><div class="comment-meta"><span>Posted by: Jon L.</span><span>10 hours ago</span><span class="actions"><span>Reply</span><span>Like</span></span></div></div>
      <div class="comment" style="top:62px"><span class="avatar"></span><p>Lorem ipsum dolor sit amet, consectetur adipisicing elit, sed do eiusmod tempor incididunt ut labore et dolore magna aliqua. Ut enim ad minim veniam.</p><div class="comment-meta"><span>Posted by: Jean</span><span>6 hours ago</span><span class="actions"><span>Reply</span><span>Like</span></span></div></div>
      <div class="comment" style="top:119px"><span class="avatar"></span><p>Lorem ipsum dolor sit amet, consectetur adipisicing elit, sed do eiusmod tempor incididunt ut labore et dolore magna aliqua. Ut enim ad minim veniam.</p><div class="comment-meta"><span>Posted by: Anne</span><span>10 hours ago</span><span class="actions"><span>Reply</span><span>Like</span></span></div></div>
      <span class="scroll-track" style="left:140px;height:155px"></span>
    </div>

    <div class="widget-panel panel-green" style="left:379px;width:135px">
      <div class="event" style="top:3px"><h4>SAT - Conference</h4><h5>Toronto - Canada</h5><p>Lorem ipsum dolor sit amet, consectetur adipisicing elit, sed do eiusmod tempor incididunt ut labore et dolore magna aria.</p><time>September 15th, 2015</time></div>
      <span class="event-rule" style="top:55px"></span>
      <div class="event" style="top:62px"><h4>Internet Webinar</h4><h5>Gleam +</h5><p>Lorem ipsum dolor sit amet, consectetur adipisicing elit, sed do eiusmod tempor incididunt ut labore et dolore magna aria.</p><time>October 8th, 2015</time></div>
      <span class="event-rule" style="top:113px"></span>
      <div class="event" style="top:120px"><h4>World Expo - IP</h4><h5>London - Great Britain</h5><p>Lorem ipsum dolor sit amet, consectetur adipisicing elit, sed do eiusmod tempor incididunt ut labore et dolore magna aria.</p><time>December 4th, 2015</time></div>
      <span class="scroll-track" style="left:124px;height:160px;background:#444"></span>
    </div>
  </section>

  <nav class="band footer-nav">
    <span style="left:41px">Site Map</span>
    <span style="left:132px">Contact Info</span>
    <span style="left:251px">Policies and Copyrights</span>
    <span style="left:445px">Services</span>
  </nav>

  <footer class="band site-footer">
    <ul class="footer-col" style="left:51px">
      <li>Services</li><li>Process</li><li>About Us</li><li>Services</li><li>Events</li><li>Marketing</li><li>Analitye</li><li>Media</li>
    </ul>
    <ul class="footer-col" style="left:153px">
      <li>Contact form</li><li>Address</li><li>Blog</li><li>Staff</li><li>Departments</li><li>International</li>
    </ul>
    <div class="legal-box">
      <p style="top:8px">Copyright</p>
      <p style="top:35px">VAT</p>
      <p style="top:61px">Company No.:</p>
    </div>
    <ul class="footer-col" style="left:450px">
      <li>PPC Services</li><li>SEO</li><li>Keywords</li><li>Ad Services</li><li>Tracking</li><li>Advising</li><li>Reporting</li>
    </ul>
  </footer>

</div>
</body>
</html>
```